Ferncrest Dental, LLC business card project

Business card to be designed with current logo.
Dental office- please keep design of card that looks clean and professional.
Please include the following info:
Ferncrest Dental, LLC
Dr. Lorna Pettigrew
2871 Marlowe Street
Bethlehem, PA 18093
610-555-0193
ferncrestdental.office@examplemail.test
Hello everyone-
Reason: Just got back from overseas- will look at all designs and provide feedback. Thank you!
Reason: Polling my friends for the final selection-
thank you to all those that participated- so many talented designers!

```html
<!DOCTYPE html>
<html lang="en">
<head>
<meta charset="utf-8">
<title>Ferncrest Dental, LLC — Business Card</title>
<link rel="stylesheet" href="https://fonts.googleapis.com/css2?family=Open+Sans:wght@300;400;700&display=swap">
<style>
  :root {
    --card-white: #ffffff;
    --band-green: #4cb848;
    --rail-light: #f4f4f4;
    --rail-shade: #cfcfcf;
    --name-green: #63a23f;
    --contact-lime: #a6c83a;
    --wordmark-lime: #c4de4a;
    --mark-tint: #b3d236;
  }
  * { margin: 0; padding: 0; box-sizing: border-box; }
  html, body {
    width: 1200px;
    height: 651px;
    overflow: hidden;
    background: var(--card-white);
  }
  .card {
    position: relative;
    width: 1200px;
    height: 651px;
    background: var(--card-white);
    font-family: "Open Sans", Arial, sans-serif;
    overflow: hidden;
  }
  .rail {
    position: absolute;
    left: 0;
    width: 1200px;
    background: linear-gradient(to bottom, var(--rail-light) 0%, var(--rail-shade) 55%, var(--rail-light) 100%);
  }
  .rail--top { top: 26px; height: 12px; }
  .rail--bottom { top: 355px; height: 22px; }
  .brand-band {
    position: absolute;
    left: 0;
    top: 51px;
    width: 1200px;
    height: 304px;
    background: var(--band-green);
  }
  .brand-mark {
    position: absolute;
    left: 540px;
    top: 88px;
    width: 120px;
    height: 120px;
    border-radius: 50%;
    background: var(--mark-tint);
  }
  .brand-name {
    position: absolute;
    left: 0;
    top: 246px;
    width: 1200px;
    text-align: center;
    font-weight: 300;
    font-size: 66px;
    line-height: 80px;
    letter-spacing: -1px;
    color: var(--wordmark-lime);
    white-space: nowrap;
  }
  .doctor-name {
    position: absolute;
    left: 34px;
    top: 410px;
    font-weight: 700;
    font-size: 44px;
    line-height: 52px;
    color: var(--name-green);
    white-space: nowrap;
  }
  .contact {
    position: absolute;
    right: 38px;
    top: 403px;
    text-align: right;
    font-weight: 400;
    font-size: 40px;
    line-height: 55px;
    color: var(--contact-lime);
    font-style: normal;
  }
  .contact span { display: block; white-space: nowrap; }
</style>
</head>
<body>
  <div class="card">
    <div class="rail rail--top"></div>
    <div class="brand-band"></div>
    <div class="brand-mark" aria-hidden="true"></div>
    <div class="brand-name">Ferncrest Dental, LLC</div>
    <div class="rail rail--bottom"></div>

    <div class="doctor-name">Dr. Lorna Pettigrew</div>

    <address class="contact">
      <span class="contact__street">2871 Marlowe Street</span>
      <span class="contact__city">Bethlehem, PA 18093</span>
      <span class="contact__phone">610-555-0193</span>
      <span class="contact__email">ferncrestdental.office@examplemail.test</span>
    </address>
  </div>
</body>
</html>
```